Promotional Flyer/Email Design - Cabling services for Broadcast and Audio Visual

We need a promotional flyer/email design to help launch our company, Velcor Lane. We provide cabling services for Broadcast Television and Audio Visual systems. Recent projects include major television events such as the Harrowmere Racquet Classic and Audio Visual/Entertainment systems for wealthy clients in their homes and on-board super yachts.

The flyer will be printed as single sided A5 and also be sent out in the body of a promotional email. It should feature the company logo along with a complementary colour scheme. It should have a clean finish with images that show the type of work we do (cabling and equipment installation) or the setting for these systems (tv studio, super yacht, cinema room, meeting room with projector etc.)

Services we offer are:

Broadcast/AV system design
On-site installation
Rack building
Pre-fabricated cable looms
Fibre optic installation

About the company:

Velcor Lane provide cabling services for Broadcast Television and Audio Visual systems. With over 15 years experience working in these industries we can help with every aspect of design, project managment, installation and maintenance. Our projects range from fibre optic cabling at major sports events to installing and commisioning bespoke control systems on some of the worlds largest super yachts.

Contact details:

To get a quote or discuss your project contact us now
Telephone: TBC
Email: info@velcor-lane.com
Website: www.velcor-lane.com
Address: TBC

Other information:

The company is based in London, UK. Our projects often take place in other countries with work taking place accross Europe and beyond.

We have a London based workshop for rack building and cable pre-fabrication.

Our website is www.velcor-lane.com

Images:

Images attached can be editted for use on the flyer or have ideas taken from them. Only the company logo is required to feature on the final design.

Target Market(s)

Business to business

Industry/Entity Type

It Company

Font styles to use
Sans Serif

Requirements
Must have
• Company logo
• List of services
• Contact details
Nice to have
• Image of cabling, home cinema room, super yacht, luxury home, outside broadcast truck, fibre optic equipment or cabling.

```html
<!DOCTYPE html>
<html lang="en">
<head>
<meta charset="utf-8">
<title>Velcor Lane – Broadcast &amp; AV System Installation</title>
<link rel="stylesheet" href="https://fonts.googleapis.com/css2?family=Exo+2:wght@400;600&family=Lato:wght@400;700&display=swap">
<style>
:root{
  --page:#e9e9e9;
  --paper:#ffffff;
  --ink:#333031;
  --dark-band:#3a3637;
  --grey-band:#d8d8d8;
  --red:#e3103f;
  --blue:#1b7fe6;
  --blue-band:#2086ee;
  --photo-studio:linear-gradient(180deg,#5d646c 0%,#c9ccd0 45%,#e4e6e8 100%);
  --photo-lounge:linear-gradient(160deg,#cfc6b8 0%,#9a8f82 55%,#6d645a 100%);
  --photo-panel:linear-gradient(180deg,#e8e9ea 0%,#bfc3c6 100%);
}
*{box-sizing:border-box;margin:0;padding:0}
html,body{width:1200px;height:1200px;overflow:hidden;background:var(--page)}
.flyer{position:absolute;left:195px;top:30px;width:912px;height:1283px;background:var(--paper);
  transform:scale(.8885);transform-origin:0 0;font-family:"Lato",sans-serif;color:var(--ink);overflow:hidden;
  box-shadow:0 4px 18px rgba(0,0,0,.18)}
.hero{position:absolute;left:0;top:0;width:912px;height:410px}
.brand{position:absolute;left:600px;top:160px;width:300px;display:flex;align-items:center;gap:12px;
  font-family:"Exo 2",sans-serif;font-weight:600;font-size:44px;color:var(--ink);letter-spacing:-.5px}
.brand-dot{width:22px;height:22px;border-radius:50%;background:var(--red);flex:none}
.title{position:absolute;top:425px;left:0;width:912px;text-align:center;font-family:"Exo 2",sans-serif;font-size:40px;color:var(--ink)}
.title b{font-weight:600}
.title .accent{color:var(--blue)}
.about{position:absolute;top:500px;left:0;width:912px;height:154px;background:var(--dark-band);color:#fff;
  padding:16px 38px 0 46px;font-size:19px;line-height:23.6px;text-align:justify}
.about .name{color:var(--red)}
.services-heading,.info-heading{position:absolute;font-family:"Exo 2",sans-serif;font-weight:600;font-size:26px;color:var(--blue)}
.services-heading{left:53px;top:683px;border-bottom:2px solid var(--ink);padding-bottom:2px;width:199px;white-space:nowrap}
.service-list{position:absolute;left:46px;top:738px;list-style:none}
.service-list li{display:flex;align-items:center;gap:14px;height:52.3px;font-size:21px;color:#444}
.icon{width:28px;height:28px;border-radius:50%;background:var(--red);display:flex;align-items:center;justify-content:center;flex:none}
.photo{position:absolute;border-radius:16px;box-shadow:0 3px 6px rgba(0,0,0,.3);border:3px solid #fff}
.photo-lounge{left:390px;top:698px;width:284px;height:282px;background:var(--photo-lounge)}
.photo-rack{left:690px;top:711px;width:188px;height:140px;background:var(--photo-panel)}
.photo-patch{left:697px;top:866px;width:172px;height:107px;background:var(--photo-panel)}
.info{position:absolute;left:0;top:1012px;width:912px;height:141px;background:var(--grey-band)}
.info-heading{left:57px;top:6px;border-bottom:2px solid var(--ink);padding-bottom:0;width:170px;white-space:nowrap}
.info-list{position:absolute;left:75px;top:48px;width:790px;list-style:none;font-size:19px;line-height:26px;color:#333}
.info-list li{position:relative;margin-bottom:6px}
.info-list li::before{content:"";position:absolute;left:-18px;top:10px;width:7px;height:7px;border-radius:50%;background:var(--red)}
.footer-curves{position:absolute;left:0;top:1170px;width:912px;height:113px}
.contacts{position:absolute;left:55px;top:1224px;display:flex;gap:22px;color:#fff;font-size:23px;align-items:center}
.contacts span{display:flex;align-items:center;gap:8px}
</style>
</head>
<body>
<main class="flyer">
  <svg class="hero" viewBox="0 0 912 410" aria-hidden="false">
    <defs>
      <clipPath id="hero-clip"><path d="M0 0H607V340Q607 380 567 380H40Q0 380 0 340Z"/></clipPath>
    </defs>
    <path d="M0 340Q0 400 40 400H567Q607 400 607 360V340Q607 380 567 380H40Q0 380 0 340Z" fill="var(--red)"/>
    <g clip-path="url(#hero-clip)">
      <rect width="607" height="380" fill="#c9ccd0" role="img" aria-label="Broadcast studio interior with glossy floor and colour-bar screen"/>
      <rect width="607" height="380" style="fill:url(#g)"/>
      <linearGradient id="g" x1="0" y1="0" x2="0" y2="1"><stop offset="0" stop-color="#5b6169"/><stop offset=".45" stop-color="#c6c9cd"/><stop offset="1" stop-color="#e6e8ea"/></linearGradient>
    </g>
    <circle cx="670" cy="176" r="118" fill="#fff"/>
    <path d="M642 86A100 100 0 0 0 642 266" fill="none" stroke="var(--red)" stroke-width="9" stroke-linecap="round"/>
  </svg>
  <div class="brand"><span class="brand-dot"></span>Velcor Lane</div>

  <h1 class="title"><b>Broadcast</b> &amp; <span class="accent">AV System Installation</span></h1>

  <p class="about"><span class="name">Velcor Lane</span> provide cabling services for <b>Broadcast Television and Audio Visual systems</b>. With over <b>15 years</b> experience working in these industries we can help with every aspect of design, <b>project managment, installation and maintenance</b>. Our projects range from fibre optic cabling at major sports events to installing and commisioning bespoke control systems on some of the worlds largest super yachts.</p>

  <h2 class="services-heading">Services we offer are:</h2>
  <ul class="service-list">
    <li><span class="icon"><svg width="14" height="14" viewBox="0 0 14 14"><circle cx="7" cy="5" r="2" fill="#fff"/><path d="M7 7V13M3 2A6 6 0 0 0 3 9M11 2A6 6 0 0 1 11 9" stroke="#fff" stroke-width="1.4" fill="none"/></svg></span>Broadcast/AV system design</li>
    <li><span class="icon"><svg width="14" height="14" viewBox="0 0 14 14"><path d="M2 12H12M4 12V8H10V12M6 8V2H8V8" stroke="#fff" stroke-width="1.4" fill="none"/></svg></span>On-site installation</li>
    <li><span class="icon"><svg width="14" height="14" viewBox="0 0 14 14"><rect x="2" y="2" width="10" height="10" rx="1" stroke="#fff" stroke-width="1.4" fill="none"/><path d="M2 5.5H12M2 8.5H12" stroke="#fff" stroke-width="1.2"/></svg></span>Rack building</li>
    <li><span class="icon"><svg width="14" height="14" viewBox="0 0 14 14"><path d="M3 12C3 5 7 2 12 2M6 12C6 7 9 5 12 5" stroke="#fff" stroke-width="1.4" fill="none"/></svg></span>Pre-fabricated cable looms</li>
    <li><span class="icon"><svg width="14" height="14" viewBox="0 0 14 14"><path d="M2 12L7 7M7 7L12 2M7 7L12 6M7 7L8 2M7 7L11 10" stroke="#fff" stroke-width="1.3" fill="none"/></svg></span>Fibre optic installation</li>
  </ul>

  <div class="photo photo-lounge" role="img" aria-label="Luxury living room with wall-mounted television"></div>
  <div class="photo photo-rack" role="img" aria-label="Wall-mounted distribution unit with neatly dressed cables"></div>
  <div class="photo photo-patch" role="img" aria-label="Cable looms terminated on a patch panel"></div>

  <section class="info">
    <h2 class="info-heading">Other information:</h2>
    <ul class="info-list">
      <li>The company is based in London, UK. Our projects often take place in other countries with work taking place accross Europe and beyond.</li>
      <li>We have a London based workshop for <b>rack building and cable pre-fabrication.</b></li>
    </ul>
  </section>

  <svg class="footer-curves" viewBox="0 0 912 113" aria-hidden="true">
    <path d="M72 22Q80 10 110 10H820Q880 10 885 80V90Q870 30 820 25H110Q85 25 72 22Z" fill="var(--red)"/>
    <path d="M0 36H810Q875 36 875 90V113H0Z" fill="var(--blue-band)"/>
  </svg>
  <div class="contacts">
    <span><svg width="22" height="22" viewBox="0 0 24 24"><path d="M6 3L9 7L7 9Q9 14 15 17L17 15L21 18L19 21Q10 21 3 9Z" fill="#fff"/></svg>TBC</span>
    <span><svg width="24" height="20" viewBox="0 0 24 20"><rect x="2" y="5" width="20" height="13" fill="none" stroke="#fff" stroke-width="2"/><path d="M2 5L12 12L22 5" stroke="#fff" stroke-width="2" fill="none"/></svg>info@velcor-lane.com</span>
    <span><svg width="24" height="24" viewBox="0 0 24 24"><circle cx="12" cy="12" r="9" fill="none" stroke="#fff" stroke-width="2"/><path d="M3 12H21M12 3Q6 12 12 21M12 3Q18 12 12 21" stroke="#fff" stroke-width="1.6" fill="none"/></svg>www.velcor-lane.com</span>
    <span><svg width="16" height="22" viewBox="0 0 16 22"><path d="M8 1A7 7 0 0 0 1 8C1 13 8 21 8 21S15 13 15 8A7 7 0 0 0 8 1Z" fill="#fff"/><circle cx="8" cy="8" r="2.5" fill="var(--blue-band)"/></svg>TBC</span>
  </div>
</main>
</body>
</html>
```